We are looking to recreate our Harlow & Partners Jobsite Sign. This sign will be placed by the street at each of our jobsites. We want to keep this sign simple, but at the same time, want to add a catching appeal to the design for anyone passing by. We want to stick to a two color scheme (Harlow Blue, and White). Please only use the Company Logo that I have uploaded for this project. Please also see a mock up of what we would like to include on this sign. The Sign Dimensions will be 4' x 8'. Please keep all verbiage uniform with the verbiage on the sample design I have uploaded. LET YOUR CREATIVITY FLOW!

```html
<!DOCTYPE html>
<html lang="en">
<head>
<meta charset="utf-8">
<title>Harlow &amp; Partners Jobsite Sign</title>
<link rel="stylesheet" href="https://fonts.googleapis.com/css2?family=Anton&family=Sorts+Mill+Goudy&display=swap">
<style>
  :root {
    --harlow-blue: #2e3189;
    --social-dark: #1d4f8c;
    --social-mid: #1a7cc0;
    --social-deep: #165a86;
    --sign-white: #ffffff;
    --backdrop: #e8eaf1;
  }
  * { margin: 0; padding: 0; box-sizing: border-box; }
  html, body {
    width: 1101px;
    height: 1200px;
    overflow: hidden;
    background: var(--backdrop);
  }
  .sign {
    position: absolute;
    left: 0;
    top: 325px;
    width: 1101px;
    height: 550px;
    background: var(--sign-white);
    color: var(--harlow-blue);
    font-family: "Sorts Mill Goudy", Georgia, serif;
  }
  .sign-bands { position: absolute; inset: 0; }
  .logo {
    position: absolute;
    left: 70px;
    top: 52px;
    width: 440px;
    text-align: center;
    line-height: 1;
  }
  .logo-name { font-size: 118px; display: block; }
  .logo-suffix { font-size: 50px; display: block; margin-top: -6px; }
  .divider {
    position: absolute;
    left: 541px;
    top: 58px;
    width: 5px;
    height: 162px;
    background: var(--harlow-blue);
  }
  .trade {
    position: absolute;
    left: 570px;
    top: 62px;
    width: 480px;
    text-align: center;
    font-size: 74px;
    line-height: 0.98;
    letter-spacing: 4px;
  }
  .tagline {
    position: absolute;
    left: 0;
    top: 240px;
    width: 1101px;
    height: 140px;
    display: flex;
    align-items: center;
    justify-content: center;
    font-family: "Anton", Impact, sans-serif;
    font-size: 98px;
    color: var(--sign-white);
    letter-spacing: 0.5px;
  }
  .social {
    position: absolute;
    left: 38px;
    top: 425px;
    display: flex;
    gap: 26px;
  }
  .social-item { width: 62px; text-align: center; }
  .social-square {
    display: block;
    width: 54px;
    height: 54px;
    margin: 0 auto 6px;
    border-radius: 7px;
  }
  .social-item:nth-child(1) .social-square { background: var(--social-dark); }
  .social-item:nth-child(2) .social-square { background: var(--social-mid); }
  .social-item:nth-child(3) .social-square { background: var(--social-deep); }
  .social-name { font-size: 15px; color: var(--harlow-blue); }
  .contact {
    position: absolute;
    left: 300px;
    top: 408px;
    width: 500px;
    text-align: center;
  }
  .phone {
    font-family: "Anton", Impact, sans-serif;
    font-size: 76px;
    line-height: 1;
    letter-spacing: -1px;
  }
  .website { font-size: 38px; line-height: 1; margin-top: 8px; }
  .license {
    position: absolute;
    left: 830px;
    top: 418px;
    width: 250px;
    text-align: center;
    font-size: 31px;
    line-height: 1.25;
  }
</style>
</head>
<body>
  <main class="sign">
    <svg class="sign-bands" width="1101" height="550" viewBox="0 0 1101 550" aria-hidden="true">
      <polygon points="0,0 441,0 431,26 0,26" fill="var(--harlow-blue)"/>
      <polygon points="463,0 1101,0 1101,26 453,26" fill="var(--harlow-blue)"/>
      <rect x="0" y="240" width="1101" height="140" fill="var(--harlow-blue)"/>
      <polygon points="0,525 656,525 646,550 0,550" fill="var(--harlow-blue)"/>
      <polygon points="678,525 1101,525 1101,550 668,550" fill="var(--harlow-blue)"/>
    </svg>

    <div class="logo">
      <span class="logo-name">Harlow</span>
      <span class="logo-suffix">&amp; Partners, Inc.</span>
    </div>
    <div class="divider"></div>
    <div class="trade">General<br>Contractors</div>

    <div class="tagline">We Build Client Satisfaction</div>

    <div class="social">
      <div class="social-item"><span class="social-square"></span><span class="social-name">Friendsy</span></div>
      <div class="social-item"><span class="social-square"></span><span class="social-name">Workly</span></div>
      <div class="social-item"><span class="social-square"></span><span class="social-name">Snapgram</span></div>
    </div>

    <div class="contact">
      <div class="phone">407-555-0182</div>
      <div class="website">www.harlowpartners.net</div>
    </div>

    <div class="license">CGC1048372<br>Lakeview, Florida</div>
  </main>
</body>
</html>
```